Bramble Wren Childcare centre needs a new LED outdoor banner

We need a new outdoor banner for our pre-school. It needs to be around 2440 mm x 1220 mm. It will be lit at night so I need it to stand out. I'm looking for a modern upbeat design. It will have my logo in the middle which is a graduation teddy bear with our name and phone number on it. I'm happy to experiment with different design options as mine is 20 years old. It needs to be colorful, inviting and very "in your face" and child friendly. It will be located near the fence of the property so it will be seen by cars driving by at a speed of around 50KM/H. So it needs to be clear, big bold fonts and bright colors. Thank you!

```html
<!DOCTYPE html>
<html lang="en">
<head>
<meta charset="utf-8">
<title>Bramble Wren Childcare Centre – Outdoor Banner</title>
<link rel="stylesheet" href="https://fonts.googleapis.com/css2?family=Fredoka:wght@600&family=Ubuntu:wght@700&display=swap">
<style>
  :root {
    --sky: #62fff5;
    --sun: #eaf200;
    --berry: #f414e6;
    --bubble: #5cc9f6;
    --ink: #0d0d0d;
    --cream: #ffffff;
    --bear-brown: #7d6a55;
  }
  html, body {
    margin: 0;
    padding: 0;
    width: 1200px;
    height: 600px;
    overflow: hidden;
    background: var(--sky);
  }
  .banner {
    position: relative;
    width: 1200px;
    height: 600px;
    background: var(--sky);
    overflow: hidden;
  }
  .sun-band {
    position: absolute;
    inset: 0;
    width: 1200px;
    height: 600px;
  }
  .brand {
    position: absolute;
    left: 0;
    top: 0;
    width: 1200px;
    height: 420px;
  }
  .brand-name {
    position: absolute;
    left: 0;
    top: 178px;
    width: 1200px;
    display: flex;
    justify-content: center;
    align-items: center;
    gap: 26px;
    font-family: "Fredoka", sans-serif;
    font-weight: 600;
    font-size: 128px;
    line-height: 1;
    color: var(--berry);
    margin: 0;
  }
  .brand-mark {
    width: 170px;
    height: 170px;
    border-radius: 50%;
    background: var(--bear-brown);
    flex: none;
  }
  .brand-tagline {
    position: absolute;
    left: 0;
    top: 332px;
    width: 1200px;
    text-align: center;
    font-family: "Fredoka", sans-serif;
    font-weight: 600;
    font-size: 82px;
    line-height: 1;
    color: var(--bubble);
    margin: 0;
  }
  .info {
    position: absolute;
    font-family: "Ubuntu", sans-serif;
    font-weight: 700;
    font-size: 34px;
    line-height: 36px;
    color: var(--cream);
    letter-spacing: 0.5px;
    margin: 0;
  }
  .icon { position: absolute; }
  .ages { left: 172px; top: 446px; }
  .hours { left: 172px; top: 492px; }
  .phones { left: 550px; top: 446px; }
  .address { left: 880px; top: 446px; }
  .kids-icon {
    left: 56px; top: 424px; width: 102px; height: 56px;
    background: var(--ink);
    border-radius: 28px;
  }
</style>
</head>
<body>
<main class="banner">
  <svg class="sun-band" viewBox="0 0 1200 600" aria-hidden="true">
    <polygon points="0,154 1200,146 1200,344 0,359" fill="var(--sun)"/>
  </svg>

  <section class="brand">
    <h1 class="brand-name"><span>Bramble</span><span class="brand-mark" aria-hidden="true"></span><span>Wren</span></h1>
    <p class="brand-tagline">Childcare Centre</p>
  </section>

  <div class="icon kids-icon" role="img" aria-label="Small icon of two children"></div>
  <p class="info ages">0 - 6 YEARS</p>

  <svg class="icon clock-icon" style="left:116px;top:487px" width="40" height="40" viewBox="0 0 40 40" aria-hidden="true">
    <circle cx="20" cy="20" r="17" fill="none" stroke="var(--ink)" stroke-width="4"/>
    <path d="M19 10 V22 H28" fill="none" stroke="var(--ink)" stroke-width="4" stroke-linecap="round" stroke-linejoin="round"/>
  </svg>
  <p class="info hours">7.30AM - 5.30PM</p>

  <svg class="icon phone-icon" style="left:491px;top:452px" width="44" height="44" viewBox="0 0 24 24" aria-hidden="true">
    <path d="M6.6 2.5l3 3.3-2 2.4c1.3 3 3.8 5.6 7 7.2l2.4-2 3.4 3-1.6 3.2c-.5.8-1.4 1.1-2.3.9C9.8 18.8 5 14 3.3 7.3c-.2-.9.2-1.8 1-2.3z" fill="none" stroke="var(--ink)" stroke-width="1.9" stroke-linejoin="round"/>
    <path d="M14.5 4.5a5 5 0 0 1 4.5 4.5M14.3 1.5a8 8 0 0 1 7.5 7.5" fill="none" stroke="var(--ink)" stroke-width="1.5" stroke-linecap="round"/>
  </svg>
  <p class="info phones">02 5550 1234<br>0400 555 719</p>

  <svg class="icon pin-icon" style="left:831px;top:447px" width="34" height="46" viewBox="0 0 34 46" aria-hidden="true">
    <path d="M17 0C7.6 0 0 7.4 0 16.6 0 28 17 46 17 46s17-18 17-29.4C34 7.4 26.4 0 17 0z" fill="var(--ink)"/>
    <circle cx="17" cy="16" r="6.5" fill="var(--sky)"/>
  </svg>
  <p class="info address">18 ORCHARD LN,<br>LINDEN VALE<br>NSW 2999</p>
</main>
</body>
</html>
```